Small animal veterinary clinic needs a new web site design

We need a new web site design for Harlowe Veterinary Clinic. The clinic performs medicine, surgery, and wellness care for cats and dogs. We have been in business for over 50 years so we want to project stability, reliability, class, elegance, and professionalism. We also want to convey that we have modern facilities and services and perform high quality medicine.
The current web site has been in place for many years and looks stale but for reference it is at http://www.harlowevc-example.com. We will be re-writing most of the content and looking to add additional pages, videos, downloadable documents (forms, brochures, marketing materials, etc.) The new owners prefer a more classy, modern look. Some vet clinic sites we like are http://pennfrolt.com and http://curaplumtails.com. We like a nice, clean, fresh, interactive interface.
Our new logo is attached. We want the color scheme of the web site to be complementary to the colors in the logo, especially the blue and green. The purple color of the text should just be used for accent. Upon request and if necessary, I can supply the Adobe Illustrator source file for the logo.
We are looking for a set of page designs - a great, eye-catching home page and 2-3 content page layouts we can use to create content pages with our own text and other content. Navigation design is very important as well. Again, we can fill in the content of the navigation links but I would like a nice, easy-to-use, logical navigation design. If you want some content or navigation links to use as reference during your design phase, feel free to pull whatever content or navigation you want from our existing web site. I am not looking for just images, I would like actual page files - HTML, CSS, etc.
Thanks and good luck!
Target Market(s)
We cater to pet owners across a wide age range. Socio-economic status of our customers is middle class and above. We do not target price shoppers.
Industry/Entity Type
Veterinary
Colors
Designer to choose colors to be used in the design.
Requirements
Must have
- Must look professional, clean, and modern. We are looking for simple but elegant design and navigation. 1 home page design, 2-3 content page designs delivered with code (HTML & CSS).
Nice to have
- When HTML/CSS is delivered, it would be awesome if it were mobile ready as well.
Should not have
- Colors that are too bold. Layout that is too complex.

```html
<!DOCTYPE html>
<html lang="en">
<head>
<meta charset="utf-8">
<title>Harlowe Veterinary Clinic</title>
<link href="https://fonts.googleapis.com/css2?family=Noto+Sans:wght@400;700&family=Open+Sans:wght@400;600&family=Tinos:wght@700&family=Roboto:wght@400;500;700&display=swap" rel="stylesheet">
<style>
:root{
  --green:#31a878;
  --green-dark:#1b8a5c;
  --green-pale:#c9f3df;
  --purple:#4a1038;
  --purple-btn:#6a1446;
  --blue:#3c8ee0;
  --blue-light:#4fa3f0;
  --page:#f1f1f1;
  --text:#3a3a3a;
  --white:#fff;
}
*{margin:0;padding:0;box-sizing:border-box}
html,body{width:1040px;height:1200px;overflow:hidden}
body{position:relative;background:var(--page);font-family:"Open Sans",sans-serif;color:var(--text)}
.abs{position:absolute}
.topbar{left:0;top:0;width:1040px;height:18px;background:var(--green)}
.topbar-note{right:200px;top:2px;font:600 10px "Open Sans",sans-serif;color:var(--white);letter-spacing:.3px;white-space:nowrap}
.signin{left:854px;top:0;width:56px;height:25px;background:#7a3a64;border-radius:0 0 5px 5px;color:var(--white);font:11px "Roboto",sans-serif;text-align:center;line-height:20px}
.logo-box{left:119px;top:0;width:153px;height:140px;background:var(--white);border-radius:0 0 16px 16px;box-shadow:0 1px 4px rgba(0,0,0,.15);display:flex;flex-direction:column;align-items:center;justify-content:center;gap:6px}
.logo-dot{width:14px;height:14px;border-radius:50%;background:var(--green)}
.logo-name{font:400 17px "Noto Sans",sans-serif;color:var(--purple);letter-spacing:1px}
.btn-cta{top:41px;height:35px;background:linear-gradient(#4aa2ee,#2f80d6);border-radius:3px;color:var(--white);font:700 11.5px "Roboto",sans-serif;line-height:35px;text-align:center;box-shadow:0 1px 2px rgba(0,0,0,.2);white-space:nowrap}
.nav a{position:absolute;top:100px;font:400 15px "Noto Sans",sans-serif;color:var(--purple);text-decoration:none;letter-spacing:.8px;white-space:nowrap}
.nav .active{left:314px;top:86px;width:100px;height:48px;background:var(--green-pale);border-radius:6px;color:var(--green-dark);text-align:center;line-height:50px}
.nav .active::after{content:"";position:absolute;left:42px;bottom:-7px;border:8px solid transparent;border-top-color:var(--green-pale);border-bottom:0}
.hero{left:118px;top:158px;width:802px;height:367px;background:var(--white);border-radius:4px;box-shadow:0 0 3px rgba(0,0,0,.15)}
.hero-photo{left:3px;top:2px;width:797px;height:302px;background:linear-gradient(90deg,#f3e6d8 0%,#fafafa 30%,#b07a44 55%,#f4f4f4 75%,#7fb0da 100%)}
.dots{left:363px;top:288px;width:67px;height:16px;background:var(--green);border-radius:5px 5px 0 0;display:flex;gap:4px;align-items:center;justify-content:center}
.dots i{width:10px;height:10px;border-radius:50%;background:#1e8a5e}
.dots i:first-child{background:var(--white)}
.hero-band{left:3px;top:304px;width:797px;height:61px;background:var(--green)}
.hero-title{left:22px;top:16px;width:580px;font:700 27px "Tinos",serif;color:var(--white);white-space:nowrap;letter-spacing:0}
.hero-btn{left:622px;top:12px;width:155px;height:40px;background:var(--purple-btn);border-radius:3px;color:var(--white);font:500 17px "Roboto",sans-serif;line-height:40px;text-align:center;letter-spacing:.5px}
h2.section{font:400 20px "Noto Sans",sans-serif;color:var(--purple);white-space:nowrap}
.intro{left:122px;top:600px;width:508px;font-size:11.5px;line-height:20px;text-align:justify}
.intro p+p{margin-top:20px}
.video-frame{left:670px;top:599px;width:250px;height:191px;background:var(--white);box-shadow:0 0 3px rgba(0,0,0,.2)}
.video-photo{left:3px;top:3px;width:244px;height:185px;background:linear-gradient(120deg,#dfe3ea,#a89e90 50%,#6f86b8)}
.play{left:104px;top:70px;width:42px;height:42px;border-radius:50%;background:var(--white)}
.band-shadow{left:170px;top:810px;width:700px;height:50px;border-radius:50%;background:radial-gradient(ellipse at center,rgba(0,0,0,.25),rgba(0,0,0,0) 70%)}
.band{left:118px;top:834px}
.feature h3{position:absolute;font:400 16px "Noto Sans",sans-serif;color:var(--white);white-space:nowrap}
.feature ul{position:absolute;list-style:none;font-size:11.5px;color:var(--white);white-space:nowrap}
.feature li{line-height:19px;padding-left:9px;position:relative}
.feature li::before{content:"";position:absolute;left:0;top:6px;border:3px solid transparent;border-left:4px solid var(--white);border-right:0}
.feature .thumb{position:absolute;width:76px;height:76px;border-radius:50%;border:2px solid var(--white)}
.feature .more{position:absolute;width:56px;height:16px;background:var(--green-pale);color:var(--green-dark);font:8px "Roboto",sans-serif;line-height:16px;text-align:center}
.sky{left:0;top:992px;width:1040px;height:208px;background:linear-gradient(90deg,var(--blue),var(--blue-light) 50%,var(--blue))}
.footer{left:118px;top:992px;width:804px;height:184px;background:var(--white)}
.col-shadow{top:1040px;width:20px;height:120px;background:linear-gradient(90deg,rgba(0,0,0,0),rgba(0,0,0,.1))}
.f-head{font:400 15px "Roboto",sans-serif;color:var(--purple);white-space:nowrap}
.f-list{list-style:none;font-size:11px;line-height:17.3px;color:#333}
.f-list.arrows li{padding-left:11px;position:relative}
.f-list.arrows li::before{content:"";position:absolute;left:0;top:6px;border:3px solid transparent;border-left:4px solid #999;border-right:0}
.get-touch{left:711px;top:1120px;font-size:14px}
.social{width:16px;height:16px;border-radius:50%;background:#d7d7d7;top:1122px}
.copyright{left:0;width:1040px;top:1180px;text-align:center;font:9.5px "Roboto",sans-serif;color:#e6f0fb}
.bottom-line{left:118px;top:1197px;width:804px;height:3px;background:var(--green)}
</style>
</head>
<body>

<div class="abs topbar"></div>
<div class="abs topbar-note">Sign-In to your personalized Pet Portal Today!</div>
<div class="abs signin">Sign in</div>

<div class="abs logo-box">
  <span class="logo-dot"></span>
  <span class="logo-name">HARLOWE</span>
</div>

<div class="abs btn-cta" style="left:562px;width:156px">MAKE A APPOINTMENT</div>
<div class="abs btn-cta" style="left:726px;width:196px">MAKE A RESERVATION TODAY</div>

<nav class="nav">
  <a class="active" href="#">Our Practice</a>
  <a href="#" style="left:437px">Services</a>
  <a href="#" style="left:538px">Our Staff</a>
  <a href="#" style="left:629px">Care Guides</a>
  <a href="#" style="left:735px">Contact Us</a>
  <a href="#" style="left:841px">More Info</a>
</nav>

<section class="abs hero">
  <div class="abs hero-photo" role="img" aria-label="Photo of two veterinarians smiling at a German Shepherd dog"></div>
  <div class="abs dots"><i></i><i></i><i></i><i></i></div>
  <div class="abs hero-band">
    <div class="abs hero-title">FAMILY OWNED FULL SERVICE PET CLINIC</div>
    <div class="abs hero-btn">START CARING</div>
  </div>
</section>

<h2 class="abs section" style="left:122px;top:557px">Welcome to Harlowe Veterinary Clinic</h2>
<div class="abs intro">
  <p>Harlowe Veterinary Clinic is a full-service veterinary medical hospital, located in Brookhaven, SC. The professional and courteous staff at Harlowe Veterinary Clinic seeks to provide the best possible medical care, surgical care and dental care for their highly-valued patients. We are committed to promoting responsible pet ownership, preventative health care and health-related educational opportunities for our clients.</p>
  <p>Ask us about 3 year vaccines and why they are recommended for your pet by veterinary advisory boards internationally. Drs. Hollis, Fairbrook and Dunmore strive to offer excellence in veterinary care to dogs and cats in Brookhaven and surrounding areas. Please take a moment to contact us.</p>
</div>

<h2 class="abs section" style="left:670px;top:557px">Watch Our Video</h2>
<svg class="abs" style="left:832px;top:564px" width="16" height="26" viewBox="0 0 16 26"><path d="M2 2 C6 10 9 16 8 24 M5 20 L8 24 L11 19" fill="none" stroke="#3b7fa0" stroke-width="1.2"/></svg>
<div class="abs video-frame">
  <div class="abs video-photo" role="img" aria-label="Video still of veterinarians examining a beagle">
    <div class="abs play"></div>
    <svg class="abs" style="left:120px;top:83px" width="14" height="16" viewBox="0 0 14 16"><path d="M1 0 L14 8 L1 16 Z" fill="#111"/></svg>
  </div>
</div>

<div class="abs sky"></div>
<div class="abs band-shadow"></div>
<svg class="abs band" width="804" height="162" viewBox="0 0 804 162">
  <defs><linearGradient id="bandFill" x1="0" y1="0" x2="0" y2="1"><stop offset="0" stop-color="#1b8a5c"/><stop offset="1" stop-color="#35b07e"/></linearGradient></defs>
  <path d="M0 30 Q402 -30 804 30 L804 162 Q402 155 2 158 Z" fill="url(#bandFill)"/>
</svg>

<div class="feature">
  <div class="thumb" style="left:134px;top:880px;background:linear-gradient(135deg,#f7efe2,#d9a660)" role="img" aria-label="Golden retriever and kitten"></div>
  <h3 style="left:224px;top:884px">Care Guides</h3>
  <ul style="left:228px;top:908px"><li>Exercising Your Dog</li><li>Feline Obesity</li></ul>
  <div class="more" style="left:236px;top:958px">Read More</div>

  <div class="thumb" style="left:390px;top:880px;background:linear-gradient(135deg,#a8a098,#c98040)" role="img" aria-label="Cat and puppy with a stethoscope"></div>
  <h3 style="left:480px;top:884px">Other Links</h3>
  <ul style="left:484px;top:908px"><li>Meadowvale Nutrition</li><li>Boarding and Grooming</li></ul>
  <div class="more" style="left:492px;top:957px">Read More</div>

  <div class="thumb" style="left:646px;top:880px;background:linear-gradient(135deg,#8fb07a,#3a3a3a)" role="img" aria-label="Staff member holding a small dark dog"></div>
  <h3 style="left:736px;top:884px">Our Staff</h3>
  <ul style="left:740px;top:908px"><li>Owen R. Hollis, D.V.M.</li><li>Marian T. Fairbrook</li></ul>
  <div class="more" style="left:748px;top:956px">Read More</div>
</div>

<div class="abs footer"></div>
<div class="abs col-shadow" style="left:333px"></div>
<div class="abs col-shadow" style="left:627px"></div>

<svg class="abs" style="left:177px;top:1033px" width="22" height="24" viewBox="0 0 22 24" fill="#555"><circle cx="5" cy="4" r="3"/><rect x="2" y="8" width="6" height="14" rx="1"/><rect x="12" y="2" width="2" height="20"/><rect x="14" y="5" width="6" height="2"/><rect x="14" y="12" width="6" height="2"/><rect x="14" y="19" width="6" height="2"/></svg>
<div class="abs f-head" style="left:206px;top:1034px">Our Links</div>
<ul class="abs f-list arrows" style="left:210px;top:1059px">
  <li>Our Practice</li><li>Services</li><li>Our Staff</li><li>Care Guides</li><li>Contact Us</li>
</ul>

<svg class="abs" style="left:429px;top:1036px" width="16" height="23" viewBox="0 0 16 23"><path d="M8 0 C3.5 0 0 3.5 0 8 C0 14 8 23 8 23 C8 23 16 14 16 8 C16 3.5 12.5 0 8 0 Z" fill="#555"/><circle cx="8" cy="8" r="3" fill="#fff"/></svg>
<div class="abs f-head" style="left:453px;top:1034px">Our Location</div>
<ul class="abs f-list" style="left:454px;top:1059px">
  <li>820 Linden Hollow Road</li><li>Brookhaven, SC 29400</li><li>Phone: (555) 014-2761</li><li>Fax: (555) 014-0127</li>
</ul>

<svg class="abs" style="left:696px;top:1034px" width="28" height="26" viewBox="0 0 28 26" fill="none" stroke="#555" stroke-width="1.6"><circle cx="11" cy="13" r="10"/><path d="M1 13 H21 M11 3 V23"/><rect x="19" y="6" width="7" height="14" fill="#555"/></svg>
<div class="abs f-head" style="left:733px;top:1034px">Latest News</div>
<ul class="abs f-list arrows" style="left:737px;top:1059px;width:90px">
  <li>We Offer Pet Portals!</li>
</ul>

<div class="abs f-head get-touch">Get in Touch</div>
<span class="abs social" style="left:798px"></span>
<span class="abs social" style="left:816px"></span>
<span class="abs social" style="left:834px"></span>
<span class="abs social" style="left:852px"></span>

<div class="abs copyright">Copyright © 2014 All rights reserved.</div>
<div class="abs bottom-line"></div>

</body>
</html>
```